Flyer Handout when attending Dental Conventions, or dental office shows

take the sample file folder that is shown with 2 pictures. The outside and inside of the folder needs to be completed, along with the inserts. This folder pictures are from someone elses flyer/folder and i would like to have it layout like this. The KPW inserts is informational, but it is lacking originality, pictures, etc. Try to make our information and move it to 2017. When this is done, i would like to take this flyer and load it to the web or allow to send via email and make it interactive. The user can select the flyers and it will slide or flip to the flyer. this will make if kewl/fun

Target Market(s)

Dental Offices

Industry/Entity Type

Dental

Font styles to use
Serif
Sans Serif

Colors

Designer to choose colors to be used in the design.

Requirements
Must have
• a Semi new look and feel of our flyers, and a new envelope created

```html
<!DOCTYPE html>
<html lang="en">
<head>
<meta charset="utf-8">
<title>KPW Flyer Inserts</title>
<link rel="stylesheet" href="https://fonts.googleapis.com/css2?family=Exo+2:wght@500;600&family=Lato:wght@400;700&display=swap">
<style>
:root{
  --navy:#0d4f86;
  --blue:#1774b8;
  --sky:#6fa8d6;
  --orange:#f08a1c;
  --panel:#e9e9ea;
  --ink:#2b2b2b;
  --page:#ffffff;
  --ground:#d9dadc;
}
*{margin:0;padding:0;box-sizing:border-box}
html,body{width:1200px;height:1200px;overflow:hidden;background:var(--ground)}
.sheet-set{position:relative;width:1200px;height:1200px}
.flyer{position:absolute;width:370px;height:518px;background:var(--page);overflow:hidden;font-family:"Lato",sans-serif;color:var(--ink);box-shadow:0 4px 12px rgba(0,0,0,.18)}
.f1{left:164px;top:63px}.f2{left:667px;top:63px}.f3{left:164px;top:633px}.f4{left:667px;top:633px}
.hero{position:absolute;left:0;top:0;width:370px;height:145px}
.banner-title{position:absolute;left:0;top:116px;width:370px;text-align:center;font-family:"Exo 2",sans-serif;font-weight:500;font-size:11.2px;color:#fff;letter-spacing:.2px}
.banner-title span{color:var(--orange)}
.brand{position:absolute;left:38px;top:157px;display:flex;align-items:center;gap:4px;font-family:"Exo 2",sans-serif;font-weight:600;font-size:30px;color:var(--blue);line-height:1}
.brand i{display:block;width:9px;height:9px;border-radius:50%;background:var(--orange)}
.headline{position:absolute;left:150px;top:170px;font-family:"Exo 2",sans-serif;font-weight:600;font-size:8.6px;color:var(--navy);padding-bottom:4px;border-bottom:1px solid var(--navy);line-height:1.3}
.headline span{color:var(--orange)}
.intro{position:absolute;left:39px;right:39px;top:212px;font-size:5.3px;line-height:1.3}
.intro p{margin-bottom:5px}
.intro .lead{color:var(--blue)}
.panel{position:absolute;left:0;right:0;bottom:11px;background:var(--panel);padding:10px 39px 0 39px}
.base{position:absolute;left:0;right:0;bottom:0;height:11px;background:var(--orange)}
.label{font-size:6.6px;font-weight:700;color:var(--blue);margin:0 0 5px}
.note{font-size:6px;color:var(--blue);line-height:1.3;margin-bottom:8px}
.perks{list-style:none;font-size:6.4px;line-height:1.25;margin-bottom:8px}
.perks li{position:relative;padding-left:10px;margin-bottom:3.6px}
.perks li::before{content:"";position:absolute;left:1px;top:2px;width:3.5px;height:3.5px;background:var(--orange);transform:rotate(45deg)}
.two-col{display:flex;gap:10px;margin-top:12px}
.two-col ul{flex:1}
.two-col ul+ul{border-left:1px solid #c8c8c8;padding-left:4px}
.small{font-size:5.3px;line-height:1.3;margin-bottom:7px}
.callout{border:1.5px solid var(--orange);border-radius:10px;background:#fff;text-align:center;font-size:6.2px;line-height:1.35;padding:4px 10px;margin:0 auto}
</style>
</head>
<body>
<main class="sheet-set">

<!-- Shared header artwork -->
<svg width="0" height="0" style="position:absolute">
  <defs>
    <linearGradient id="skyline" x1="0" y1="0" x2="0" y2="1">
      <stop offset="0" stop-color="#7fb0dc"/>
      <stop offset=".6" stop-color="#b9cfe0"/>
      <stop offset="1" stop-color="#5d6a73"/>
    </linearGradient>
    <g id="hero-art">
      <rect x="0" y="0" width="370" height="145" fill="#fff"/>
      <rect x="0" y="0" width="370" height="110" fill="url(#skyline)" role="img" aria-label="Photo of a suspension bridge in front of a city skyline"/>
      <polygon points="0,0 28,0 28,110 0,118" fill="var(--blue)"/>
      <polygon points="370,0 342,0 342,110 370,118" fill="var(--blue)"/>
      <polygon points="0,110 370,110 370,122 360,140 10,140 0,122" fill="var(--navy)"/>
    </g>
  </defs>
</svg>

<article class="flyer f1">
  <svg class="hero" viewBox="0 0 370 145"><use href="#hero-art"/></svg>
  <div class="banner-title">BRIDGING THE GAP BETWEEN <span>PAYERS AND PROVIDERS</span></div>
  <div class="brand">KPW<i></i></div>
  <div class="headline">Introducing Accounts <span>Receivable Aging</span></div>
  <div class="intro">
    <p>At KPW we are proud to announce a NEW Portal feature.</p>
    <p>KPW Accounts Receivable Aging: Are you spending too much time on the phone with insurance companies trying to figure out why your claims are not paid? KPW has a wonderful AR Aging integration that will reduce your time on the phone by 50 – 75%.</p>
    <p>Currently your office goes into your dental software and creates a report for all of your outstanding insurance claims and then prints the report to paper. It is sorted by insurance company and starting with Northfield Mutual. The insurance person would call on the first claim, Laura Bennett, who has Northfield Mutual. Go through all the prompts and now wait on hold until they get a customer service rep. And now come to find out that the patient didn't have coverage, or they never received the claim, or whatever else is wrong.</p>
    <p>KPW has streamlined this process. We are able to reconcile the outstanding insurance claims from your Dental Software to our clearinghouse and can tell what has been Paid, Rejected, and or Processed. It saves about 50 - 75% of time being spent on the phone. What is also nice about this service is that this is Web Based, and users can be at home, in the office at another computer and or be on vacation and still have access to their outstanding claims.</p>
  </div>
  <section class="panel" style="top:347px">
    <p class="note">If your staff doesn't have time to follow up with your AR Aging, than ask KPW to manage your claims. KPW will report back the results of all of your outstanding insurance claims in a single report.</p>
    <p class="label" style="font-weight:400">Features/Benefits</p>
    <div class="two-col">
      <ul class="perks">
        <li>Online Tracking of your claims</li>
        <li>Easy 1 click to check the status of your claims</li>
        <li>Ability to correct and resubmit or just resubmit your claims</li>
      </ul>
      <ul class="perks">
        <li>Options to track your claim results and enter notes into the claim</li>
        <li>Easy integration</li>
        <li>Eliminates time being spent on the phone with insurance companies</li>
      </ul>
    </div>
    <p class="callout" style="margin-top:2px">For as low as $49.95 per month. If you have questions, Call us today at (800) 555-0142 option 2</p>
  </section>
  <div class="base"></div>
</article>

<article class="flyer f2">
  <svg class="hero" viewBox="0 0 370 145"><use href="#hero-art"/></svg>
  <div class="banner-title">BRIDGING THE GAP BETWEEN <span>PAYERS AND PROVIDERS</span></div>
  <div class="brand">KPW<i></i></div>
  <div class="headline" style="top:162px">At KPW we are proud to announce<br>a <span>NEW</span> feature for offices.</div>
  <div class="intro" style="top:210px">
    <p><span class="lead">KPW Auto-Post:</span> Payment posting that accelerates the revenue cycle by automatically posting payments for virtually any payer that provides electronic EOB's. If you are receiving your EOB's on the KPW Portal or would like to receive, you can now post them directly into your Dental Software Package.</p>
    <p>Our expert staff will work closely with each client to create a customized Auto Post solution in the KPW Bridge that will interface with your Dental Software Package. Auto-Post will post primary and secondary claims, contractual adjustments, rejection notes, and claims status notes. The results of this combination are very significant and will benefit your office and increase efficiency.</p>
  </div>
  <section class="panel" style="top:280px">
    <p class="label">FEATURES:</p>
    <ul class="perks">
      <li>Automated payment posting for participating Government and Commercial payers</li>
      <li>Robust decision support</li>
      <li>Tailored error and exception rules</li>
      <li>Customized solutions that work with any existing Dental Software</li>
      <li>Easy integration</li>
    </ul>
    <p class="label">BENEFITS:</p>
    <ul class="perks">
      <li>Detailed reporting every step of the way</li>
      <li>Elimination of manual data entry</li>
      <li>Automation that saves time and reduces errors</li>
      <li>Fast identification of claim discrepancies</li>
      <li>Customizable solutions that fit any provider's business needs</li>
    </ul>
    <p class="callout" style="width:276px;margin-top:14px">To get started with our special offer of .15¢ per claim or if you have questions,<br>Call us today at (800) 555-0142 ext.800</p>
  </section>
  <div class="base"></div>
</article>

<article class="flyer f3">
  <svg class="hero" viewBox="0 0 370 145"><use href="#hero-art"/></svg>
  <div class="banner-title">BRIDGING THE GAP BETWEEN <span>PAYERS AND PROVIDERS</span></div>
  <div class="brand">KPW<i></i></div>
  <div class="headline">Introducing KPW Real-<span>Time Eligibility</span></div>
  <div class="intro" style="top:210px">
    <p>We are proud to announce a NEW feature.</p>
    <p>You are now able to process real-time eligibility. This service is an easy-to-use solution providing instant connectivity to leading commercial and government insurers. This service will help you to automate time-consuming business functions while improving patient services.</p>
    <p>KPW real-time eligibility consolidates access to multiple payers from a single screen with the one source solution, it allows dental offices to receive eligibility and plan benefit information immediately from insurance companies. Most importantly, the eligibility information received is displayed in an understandable, easy to read format that can be printed and shared with your patient.</p>
  </div>
  <section class="panel" style="top:285px">
    <p class="label">BENEFITS:</p>
    <ul class="perks">
      <li>Decrease the amount of phone calls to insurance companies</li>
      <li>Improve your patient services by knowing at the time of service what is owed</li>
      <li>Expedite reimbursements</li>
      <li>Increase cash flow</li>
      <li>Improve dental claims acceptance rates</li>
    </ul>
    <p class="label" style="margin-top:14px">HOW IT WORKS:</p>
    <p class="small">Within KPW Bridge, select the NEW Eligibility Tab, Hit send and you will begin receiving all of your eligibility responses within the KPW Portal. It is that easy!</p>
    <p class="label">IMPLEMENTATION:</p>
    <p class="small">Please contact KPW support and we will activate your eligibility service within the KPW Bridge and the KPW Portal within minutes.</p>
    <p class="callout" style="width:276px;margin-top:14px">To find out more information or have any questions about this feature answered<br>please call (800) 555-0142</p>
  </section>
  <div class="base"></div>
</article>

<article class="flyer f4">
  <svg class="hero" viewBox="0 0 370 145"><use href="#hero-art"/></svg>
  <div class="banner-title">BRIDGING THE GAP BETWEEN <span>PAYERS AND PROVIDERS</span></div>
  <div class="brand">KPW<i></i></div>
  <div class="headline">Introducing KPW Statement <span>Processing</span></div>
  <div class="intro" style="top:205px">
    <p>KPW is proud to announce a NEW feature:</p>
    <p>KPW Statement Processing provides clear, concise patient statements that create effective patient communications. Focus on improving the quality of how patients view statements. These easy-to-read billing statements help educate patients on their financial responsibilities, resulting in a higher payment rate and reduced customer service calls.</p>
    <p>KPW provides Processing, Printing, Inserting, Return Remittance Envelope, Mailing, and postage at first class bulk presort rate. ** Included with service is national postal service AddressTrack technology which provides address forwarding for any listed change of addresses. This feature reduces cost and undeliverable mail. **</p>
  </div>
  <section class="panel" style="top:285px;padding-top:8px">
    <p class="label">FEATURES:</p>
    <ul class="perks" style="margin-bottom:3px">
      <li>Custom statement designs</li>
      <li>Full color printing options</li>
      <li>Backer/Duplex included in service; providing convenient marketing/custom office policies</li>
      <li>Online statement and document viewing through the KPW Portal</li>
      <li>Online access to your statement reports with patient address updates through the Portal</li>
    </ul>
    <p class="label">BENEFITS:</p>
    <ul class="perks" style="margin-bottom:6px">
      <li>Provides clear, concise financial statements</li>
      <li>Reduces customer service calls</li>
      <li>Saves money and time</li>
      <li>Helps improve cash flow through prompt billing</li>
      <li>Keeps the office in contact with past due accounts</li>
      <li>Reduces the necessity of maintaining a large inventory of mailing materials</li>
      <li>Decreases undeliverable mail and speeds collections by using the most current address information available.</li>
    </ul>
    <p class="callout" style="width:290px">Statements pricing is only $.68 per single printed page or email. For more information<br>Please call (800) 555-0142 ext.808 or send email to: statements@kpwdental.com</p>
  </section>
  <div class="base"></div>
</article>

</main>
</body>
</html>
```